Prayer Service 12.28.2013

I need a flyer designed for a Christian prayer service. The title and theme is:
"Total and Complete Surrender for Total and Complete Deliverance!"
1. You have creative freedom with imagery and typography
2. I need a quick turnaround time
FLYER DETAILS:
A prayer, anointing, and deliverance all night prayer service, at Brookhaven Assembly.
Saturday December 28 2013 from 9pm-6am.
Special guest speakers, prayer,anointing,and deliverance sessions.
For more information contact Sis Mirela Thornbury at Brookhaven Assembly 347 562 1094 Ext. 4816 or Janelle Corbin at 631 538-2904

```html
<!DOCTYPE html>
<html lang="en">
<head>
<meta charset="utf-8">
<title>Total and Complete Surrender – All Night Prayer Service</title>
<link rel="stylesheet" href="https://fonts.googleapis.com/css2?family=Parisienne&family=Fira+Sans:wght@400;700&display=swap">
<style>
  :root {
    --ink: #1c1712;
    --sky-top: #b9b6c4;
    --sky-mid: #e6d3b8;
    --glow: #fff4d6;
    --ember: #d9582e;
    --amber: #f0a53a;
    --parchment: #e6c98c;
    --parchment-deep: #c9a45e;
    --hands-light: #e9c9a0;
    --hands-deep: #b98d66;
  }
  * { margin: 0; padding: 0; box-sizing: border-box; }
  html, body { width: 900px; height: 1200px; overflow: hidden; background: #e9e9e9; }
  .flyer {
    position: relative;
    width: 900px;
    height: 1200px;
    overflow: hidden;
    color: var(--ink);
    background: linear-gradient(180deg, var(--parchment) 0%, var(--parchment-deep) 100%);
  }
  .flyer__sky {
    position: absolute; left: 0; top: 0; width: 900px; height: 560px;
    background:
      radial-gradient(ellipse 340px 240px at 300px 430px, var(--glow) 0%, rgba(255,240,200,0.6) 45%, rgba(255,240,200,0) 100%),
      radial-gradient(ellipse 300px 130px at 760px 390px, rgba(217,88,46,0.75) 0%, rgba(217,88,46,0) 100%),
      linear-gradient(180deg, var(--sky-top) 0%, var(--sky-mid) 60%, #f1d6a8 100%);
  }
  .flyer__hands {
    position: absolute; left: 0; top: 560px; width: 900px; height: 340px;
    background: linear-gradient(180deg, #f1d6a8 0%, var(--hands-light) 35%, var(--hands-deep) 70%, var(--parchment) 100%);
  }
  .title {
    display: block;
    position: absolute; left: 0; width: 100%;
    text-align: center;
    font-family: "Parisienne", cursive;
    font-weight: 400;
    line-height: 1;
    white-space: nowrap;
  }
  .title--lead { font-size: 76px; }
  .title--surrender { font-size: 140px; top: 110px; }
  .title--joiner { font-size: 56px; top: 250px; }
  .title--lead-1 { top: 30px; }
  .title--lead-2 { top: 310px; }
  .title--deliverance { font-size: 158px; top: 380px; }
  .details {
    position: absolute; left: 0; width: 100%; top: 925px;
    text-align: center;
    font-family: "Fira Sans", sans-serif;
  }
  .details__headline { font-size: 31px; font-weight: 700; line-height: 1.22; }
  .details__date { font-size: 25px; font-weight: 700; margin-top: 24px; }
  .details__program { font-size: 18px; margin-top: 2px; }
  .details__contact { font-size: 19px; line-height: 1.3; margin-top: 18px; }
</style>
</head>
<body>
<main class="flyer">
  <div class="flyer__sky" role="img" aria-label="Glowing sunrise sky with red and orange clouds"></div>
  <div class="flyer__hands" role="img" aria-label="Two open hands raised in surrender with a dove flying between them"></div>

  <h1>
    <span class="title title--lead title--lead-1">Total and Complete</span>
    <span class="title title--surrender">Surrender</span>
    <span class="title title--joiner">for</span>
    <span class="title title--lead title--lead-2">Total and Complete</span>
    <span class="title title--deliverance">Deliverance!</span>
  </h1>

  <section class="details">
    <p class="details__headline">A prayer, anointing, and deliverance all night<br>prayer service, at Brookhaven Assembly.</p>
    <p class="details__date">Saturday December 28 2013 from 9pm-6am.</p>
    <p class="details__program">Special guest speakers, special music, prayer,anointing,and deliverance sessions.</p>
    <p class="details__contact">For more information contact Sis Mirela Thornbury at Brookhaven Assembly<br>347 562 1094 Ext. 4816 or Janelle Corbin at 631 538-2904</p>
  </section>
</main>
</body>
</html>
```